Professional Services - letterhead / business cards

The company (velmora holdings) will provide services to Investment Funds and large investors in Spain. I have recently chosen a logo that I am attaching.

I would like a simple stationary design that i could use as letter head, business cards and "with compliments" cards.

I am not quite sure which color I will mostly use for the logo, in the email signature I will probably lean towards the white background and grey letters. I am attaching my favourite options.

Target Market(s)

Large Multinationals, Investment funds and Law firms

Industry/Entity Type

Business

Requirements
Must have
• my details are:
Luis R. Albarda
Velmora Holdings S.L.
Casa de Valdetorres
Calle de Ortuzar Beltrán 27
28019 Madrid
T: +34 (91) 387-6051
M: +34 (655) 814-073
e-mail: lalbarda@velmoraholdings.example

```html
<!DOCTYPE html>
<html lang="en">
<head>
<meta charset="utf-8">
<title>Velmora Holdings — Stationery</title>
<link rel="stylesheet" href="https://fonts.googleapis.com/css2?family=Questrial&family=Didact+Gothic&display=swap">
<style>
  :root{
    --navy:#2b2a6b;
    --violet:#3d3b8e;
    --violet-light:#7a76b0;
    --paper:#ffffff;
    --paper-shade:#f4f4f5;
    --ink-grey:#7d7d86;
    --wash:#ecedf0;
    --window:#dcdcdf;
    --stage:#e6e6e9;
    --rule:#b8b8c0;
  }
  *{box-sizing:border-box;margin:0;padding:0}
  html,body{width:1200px;height:808px;overflow:hidden}
  body{background:var(--stage);font-family:"Questrial",sans-serif;color:var(--navy);position:relative}
  .sheet{position:absolute;background:var(--paper);overflow:hidden;box-shadow:0 2px 8px rgba(0,0,0,.12)}
  .wordmark{position:absolute;font-family:"Questrial",sans-serif;color:var(--navy);white-space:nowrap;letter-spacing:.01em}
  .watermark{position:absolute;font-family:"Questrial",sans-serif;color:var(--wash);white-space:nowrap;line-height:1}
  .web{position:absolute;font-family:"Didact Gothic",sans-serif;color:var(--ink-grey);white-space:nowrap}
  .web b{color:var(--navy);font-weight:normal}
  .contact{position:absolute;font-family:"Didact Gothic",sans-serif;color:var(--ink-grey);line-height:1.45;white-space:nowrap}
  .contact .company{font-family:"Questrial",sans-serif;color:var(--navy);font-weight:bold}
  .contact .row{display:flex;align-items:center;gap:4px}
  .contact svg{width:1em;height:1em;fill:var(--navy);flex:none}

  /* letterhead */
  .letterhead{left:24px;top:36px;width:520px;height:736px}
  .letterhead .wordmark{left:34px;top:92px;font-size:27px}
  .letterhead .contact{right:40px;top:48px;font-size:9px}
  .letterhead .contact .company{font-size:11px}
  .letterhead .watermark{left:20px;bottom:4px;font-size:150px}
  .letterhead .web{right:34px;bottom:26px;font-size:8px}

  /* business cards */
  .card-front{left:572px;top:88px;width:292px;height:168px}
  .card-front .wordmark{left:24px;top:52px;font-size:18px}
  .card-front .holder{position:absolute;right:24px;top:92px;text-align:right;font-size:10px;line-height:1.2}
  .card-front .holder strong{display:block;font-size:11px}
  .card-front .holder-rule{position:absolute;left:150px;right:24px;top:118px;border-top:1px solid var(--rule)}
  .card-front .contact{left:24px;bottom:14px;font-size:7px}
  .card-back{left:884px;top:88px;width:292px;height:168px;background:linear-gradient(120deg,var(--violet) 0%,var(--violet) 35%,var(--violet-light) 100%)}
  .card-back .web{right:20px;top:18px;font-size:8px;color:#fff}
  .card-back .web b{color:#fff}
  .card-back .watermark{left:6px;bottom:16px;font-size:78px;color:rgba(255,255,255,.12)}

  /* window envelope */
  .envelope-front{left:572px;top:276px;width:604px;height:286px;background:var(--paper-shade)}
  .envelope-front .wordmark{left:40px;top:62px;font-size:26px}
  .envelope-front .address-window{position:absolute;left:46px;top:126px;width:272px;height:88px;border-radius:14px;background:var(--window)}
  .envelope-front .watermark{left:10px;bottom:30px;font-size:150px}
  .envelope-front .web{right:30px;bottom:22px;font-size:8px}

  /* compliment slip */
  .compliment-slip{left:572px;top:582px;width:292px;height:138px;background:var(--paper-shade)}
  .compliment-slip .web{right:14px;top:12px;font-size:5.5px}
  .compliment-slip .watermark{left:0;bottom:0;font-size:74px}
  .compliment-slip .wordmark{left:16px;top:36px;font-size:13px}
  .compliment-slip .greeting{position:absolute;right:14px;top:82px;font-size:9px;white-space:nowrap}
  .compliment-slip .greeting strong{font-size:13px;font-weight:bold}
  .compliment-slip .contact{left:16px;bottom:10px;font-size:5.5px}

  /* envelope back */
  .envelope-back{left:884px;top:582px;width:292px;height:138px}
  .envelope-back svg.flap{position:absolute;left:0;top:0;width:292px;height:138px}
  .envelope-back .wordmark{left:108px;top:30px;font-size:12px;color:#fff}
  .envelope-back .contact{left:0;right:0;bottom:8px;font-size:5.5px;text-align:center}
  .envelope-back .contact .company{font-size:7px}
  .envelope-back .contact .row{justify-content:center}
</style>
</head>
<body>

<svg width="0" height="0" style="position:absolute" aria-hidden="true">
  <symbol id="icon-pin" viewBox="0 0 10 10"><path d="M5 0a3.5 3.5 0 0 0-3.5 3.5C1.5 6 5 10 5 10s3.5-4 3.5-6.5A3.5 3.5 0 0 0 5 0zm0 4.8a1.3 1.3 0 1 1 0-2.6 1.3 1.3 0 0 1 0 2.6z"/></symbol>
  <symbol id="icon-phone" viewBox="0 0 10 10"><path d="M1 3.5C1 2 2.5 1 5 1s4 1 4 2.5L7.5 4.3 6.5 3H3.5L2.5 4.3zM2.5 5h5l1 4h-7z"/></symbol>
  <symbol id="icon-mobile" viewBox="0 0 10 10"><path d="M3 0.5h4a.8.8 0 0 1 .8.8v7.4a.8.8 0 0 1-.8.8H3a.8.8 0 0 1-.8-.8V1.3A.8.8 0 0 1 3 .5zm.3 1.2v5.8h3.4V1.7z"/></symbol>
  <symbol id="icon-mail" viewBox="0 0 10 10"><path d="M0.5 2h9v6h-9zM1.3 2.6 5 5.4l3.7-2.8z"/></symbol>
</svg>

<!-- Letterhead -->
<section class="sheet letterhead" aria-label="Letterhead">
  <div class="watermark" aria-hidden="true">velmora</div>
  <div class="wordmark">velmora holdings</div>
  <div class="contact">
    <div class="company">Velmora Holdings S.L.</div>
    <div class="row"><svg><use href="#icon-pin"/></svg>Calle de Ortuzar Beltrán 27 28019 Madrid</div>
    <div class="row"><svg><use href="#icon-phone"/></svg>+34 (91) 387-6051</div>
    <div class="row"><svg><use href="#icon-mail"/></svg>lalbarda@velmoraholdings.example</div>
  </div>
  <div class="web">www.<b>velmoraholdings</b>.example</div>
</section>

<!-- Business card, front -->
<section class="sheet card-front" aria-label="Business card front">
  <div class="wordmark">velmora holdings</div>
  <div class="holder"><strong>Luis R. Albarda</strong>President</div>
  <div class="holder-rule"></div>
  <div class="contact">
    <div class="row"><svg><use href="#icon-pin"/></svg>Calle de Ortuzar Beltrán 27 28019 Madrid</div>
    <div class="row"><svg><use href="#icon-phone"/></svg>+34 (91) 387-6051 <svg><use href="#icon-mobile"/></svg>+34 (655) 814-073</div>
    <div class="row"><svg><use href="#icon-mail"/></svg>lalbarda@velmoraholdings.example</div>
  </div>
</section>

<!-- Business card, back -->
<section class="sheet card-back" aria-label="Business card back">
  <div class="watermark" aria-hidden="true">velmora</div>
  <div class="web">www.<b>velmoraholdings</b>.example</div>
</section>

<!-- Window envelope -->
<section class="sheet envelope-front" aria-label="Window envelope front">
  <div class="watermark" aria-hidden="true">velmora</div>
  <div class="wordmark">velmora holdings</div>
  <div class="address-window"></div>
  <div class="web">www.<b>velmoraholdings</b>.example</div>
</section>

<!-- Compliment slip -->
<section class="sheet compliment-slip" aria-label="With compliments slip">
  <div class="watermark" aria-hidden="true">velmora</div>
  <div class="web">www.<b>velmoraholdings</b>.example</div>
  <div class="wordmark">velmora holdings</div>
  <div class="greeting">With<strong>Compliment</strong></div>
  <div class="contact">
    <div class="row"><svg><use href="#icon-pin"/></svg>Calle de Ortuzar Beltrán 27 28019 Madrid</div>
    <div class="row"><svg><use href="#icon-phone"/></svg>+34 (91) 387-6051 <svg><use href="#icon-mobile"/></svg>+34 (655) 814-073</div>
    <div class="row"><svg><use href="#icon-mail"/></svg>lalbarda@velmoraholdings.example</div>
  </div>
</section>

<!-- Envelope back -->
<section class="sheet envelope-back" aria-label="Envelope back">
  <svg class="flap" viewBox="0 0 292 138" aria-hidden="true">
    <defs>
      <linearGradient id="flap-fill" x1="0" y1="0" x2="1" y2="0">
        <stop offset="0" stop-color="var(--violet)"/>
        <stop offset=".55" stop-color="var(--violet)"/>
        <stop offset="1" stop-color="var(--violet-light)"/>
      </linearGradient>
    </defs>
    <path d="M6 136 L70 66 M292 40 L232 72" stroke="var(--rule)" stroke-width=".6" fill="none"/>
    <path d="M0 0 H292 V20 C250 22 228 40 200 58 C170 74 120 74 70 64 C40 58 18 48 0 46 Z" fill="url(#flap-fill)"/>
  </svg>
  <div class="wordmark">velmora holdings</div>
  <div class="contact">
    <div class="company">Velmora Holdings S.L.</div>
    <div class="row"><svg><use href="#icon-pin"/></svg>Calle de Ortuzar Beltrán 27 28019 Madrid</div>
    <div class="row"><svg><use href="#icon-phone"/></svg>+34 (91) 387-6051 <svg><use href="#icon-mail"/></svg>lalbarda@velmoraholdings.example</div>
  </div>
</section>

</body>
</html>
```